Website Design and Build

This is a design and build of a dating site.

100% the most important thing is for the website to look good. I want this thing to be stunning and feel like a premium product so please only tender for the job if you excel at design and use of colours.

Theme is: premium, professional & uncluttered
Colour Scheme is: bright, fun and friendly but also reassuring and professional
 
Platforms: Initially just browser based (desktop and mobile) but if the proof of concept works we will roll it out to apps across the major platforms.

Marketing will be done primarily through organic online searches and content driven leads to a squeeze page, so SEO optimisation and experience with squeeze pages also a must.

Please include examples of sites you’ve done or other sites you think give a flavour of your vision for what this site will be. Any thoughts on palettes/colour scheme also useful.

I will provide the full brief to the successful designer.

Thank you for your time.

Industry/Entity Type

Dating

Coding

Coded - Design and coding required

Number of Pages Required

5+ page

Font styles to use
Sans Serif

Colors

Designer to choose colors to be used in the design.

Requirements
Must have
• Professional, Premium and uncluttered look.
• SEO optimisation.
• Squeeze page.
• A way to track different lead sources e.g. some of it will be content led to a squeeze page, some of it organic search engine hits, some of it unique referral links given to specific bloggers/influencers. I want to be able to track the success of all the different types of generating traffic to the site.
• I also want to be able to amend/update the site myself going forward so would like the spec/design to be clearly documented to allow me to do this.

```html
<!DOCTYPE html>
<html lang="en">
<head>
<meta charset="utf-8">
<title>Heartline — Find The Perfect Match</title>
<link href="https://fonts.googleapis.com/css2?family=Raleway:wght@400;500;600;700&family=Open+Sans:ital,wght@0,400;0,600;0,700;1,400;1,600&family=Roboto+Slab:wght@600&display=swap" rel="stylesheet">
<style>
:root{
  --gold:#e9b82f;
  --gold-soft:#f0c94f;
  --plum:#35183f;
  --plum-deep:#2a1133;
  --plum-mid:#4a2458;
  --cream:#f3efe4;
  --ink:#222222;
  --muted:#8a8a8a;
  --white:#ffffff;
  --header:#e9e9e9;
}
*{box-sizing:border-box;margin:0;padding:0}
html,body{width:1200px;height:3822px;overflow:hidden}
body{font-family:"Open Sans",Arial,sans-serif;color:var(--ink);background:var(--white)}
section,header,footer{position:relative;width:1200px;overflow:hidden}
.abs{position:absolute}
.photo{position:absolute;background:linear-gradient(135deg,#b9a58e,#6d5a52)}
h1,h2,h3{font-family:"Raleway",Arial,sans-serif;font-weight:400}

/* header */
.site-header{height:112px;background:var(--header)}
.brand{position:absolute;left:0;width:1200px;top:24px;text-align:center;font-family:"Raleway",sans-serif;font-weight:600;font-size:22px;color:var(--gold)}
.brand::before{content:"";display:inline-block;width:16px;height:16px;border-radius:50%;background:var(--gold);margin-right:10px;vertical-align:-1px}
.main-nav{position:absolute;top:78px;left:452px;display:flex;gap:30px;font-size:14px;font-weight:600}
.nav-tools{position:absolute;top:70px;left:804px;display:flex;gap:20px;align-items:center}

/* hero */
.hero{height:609px;background:var(--gold)}
.hero-photo{left:0;top:0;width:538px;height:609px;background:linear-gradient(120deg,#5fa3a3 0%,#8a6f5d 45%,#a02a35 70%,#3a3f48 100%)}
.hero-bars{position:absolute;left:538px;top:0;width:662px;height:609px;background:repeating-linear-gradient(90deg,rgba(255,255,255,.0) 0 60px,rgba(255,255,255,.08) 60px 90px)}
.hero h1{position:absolute;left:609px;top:50px;font-size:31px;line-height:38px;color:var(--ink)}
.hero h1 strong{font-weight:700;display:inline-block;border-bottom:3px solid var(--ink);padding-bottom:2px}
.hero-lead{left:611px;top:142px;width:370px;font-size:13px;line-height:20px;color:#4a3a12}
.field{position:absolute;left:611px;width:270px;height:36px;background:rgba(255,255,255,.28);font-size:12px;padding:10px 14px;color:#4a3a12}
.btn-signup{position:absolute;left:611px;top:361px;width:270px;height:38px;background:var(--plum);color:var(--white);font-size:16px;text-align:center;line-height:38px}
.latest{left:611px;top:421px;font-size:13px;font-weight:600}
.latest-arrows{left:996px;top:419px;font-size:14px}
.avatar{position:absolute;top:461px;width:110px;height:110px;border-radius:50%;border:4px solid var(--white);background:linear-gradient(135deg,#cfc4b8,#56606b)}

/* members */
.members{height:482px;background:var(--plum)}
.section-kicker{position:absolute;left:0;width:1200px;text-align:center;font-family:"Raleway",sans-serif;font-size:25px}
.section-title{position:absolute;left:0;width:1200px;text-align:center;font-family:"Raleway",sans-serif;font-weight:700;font-size:25px}
.members .section-kicker,.members .section-title{color:var(--white)}
.member-tile{top:168px;width:194px;height:222px}
.discover{left:0;width:1200px;top:424px;text-align:center;color:var(--white);font-family:"Raleway",sans-serif;font-size:17px;letter-spacing:1px}

/* community */
.community{height:662px;background:var(--cream)}
.centered-copy{position:absolute;left:0;width:1200px;text-align:center;font-size:13px;line-height:26px;color:#444}
.tabs{position:absolute;left:476px;top:216px;display:flex;gap:4px}
.tab{height:28px;padding:0 10px;border:1px solid #ccc;background:var(--white);font-size:11px;line-height:26px}
.tab.is-active{background:var(--gold);border-color:var(--gold);color:var(--white)}
.group{position:absolute;width:420px;height:140px}
.group-pic{position:absolute;left:0;top:0;width:140px;height:140px;border-radius:50%;background:linear-gradient(135deg,#e2c9a8,#7c4f3a)}
.group-badge{position:absolute;left:-8px;top:4px;width:50px;height:50px;border-radius:50%;background:var(--white);border:1px solid #ddd;text-align:center;font-size:8px;line-height:12px;padding-top:13px;color:#555}
.group-badge b{display:block;font-size:11px;color:var(--ink)}
.group-name{position:absolute;left:150px;top:20px;font-size:15px;font-weight:600}
.group-text{position:absolute;left:150px;top:46px;width:230px;font-size:11px;line-height:18px;color:var(--muted)}
.group-link{position:absolute;left:150px;top:86px;font-size:10px;font-weight:700}

/* events */
.events{height:454px;background:var(--white)}
.events-shadow{left:230px;top:72px;width:405px;height:285px;background:#2d2d30}
.events-photo{left:204px;top:72px;width:405px;height:285px;background:linear-gradient(135deg,#c0275a,#6b2a7a 55%,#2b1640)}
.split-kicker{position:absolute;font-family:"Raleway",sans-serif;font-size:25px}
.split-title{position:absolute;font-family:"Raleway",sans-serif;font-weight:700;font-size:25px;padding-bottom:6px;border-bottom:2px solid var(--ink)}
.split-copy{position:absolute;width:330px;font-size:12px;line-height:22px;color:#555}
.btn-gold{position:absolute;background:var(--gold);color:var(--white);font-size:11px;font-weight:700;text-align:center}

/* near */
.near{height:308px;background:linear-gradient(180deg,#3c1b48,#2c1236)}
.near h2{position:absolute;left:0;width:1200px;top:58px;text-align:center;color:var(--white);font-weight:700;font-size:25px}
.location{position:absolute;left:318px;top:122px;width:485px;height:38px;border:1px solid rgba(255,255,255,.35);color:rgba(255,255,255,.7);font-size:13px;padding:10px 14px}
.location svg{position:absolute;right:14px;top:14px}
.btn-find{position:absolute;left:810px;top:122px;width:69px;height:38px;background:var(--gold);color:var(--white);font-size:11px;font-weight:700;text-align:center;line-height:38px}
.place{position:absolute;top:203px;width:78px;height:78px;border-radius:50%;border:3px solid var(--white);background:linear-gradient(135deg,#9fb6c8,#4e5e6b)}

/* matchmaking */
.matching{height:461px;background:var(--cream)}
.match-card{position:absolute;left:199px;top:71px;width:430px;height:298px;background:var(--white);border:1px solid #ddd}
.match-photo{position:absolute;top:0;width:214px;height:240px}
.match-score{position:absolute;left:171px;top:174px;width:88px;height:88px;background:var(--gold);transform:rotate(45deg);border-radius:6px}
.match-score span{position:absolute;left:0;top:0;width:88px;height:88px;transform:rotate(-45deg);color:var(--white);font-weight:700;font-size:21px;text-align:center;line-height:88px}
.match-name{position:absolute;top:256px;width:214px;text-align:center;font-family:"Roboto Slab",serif;font-size:13px;font-weight:600}

/* values */
.values{height:398px;background:var(--white)}
.value{position:absolute;top:181px;width:300px;text-align:center}
.value-icon{width:112px;height:76px;margin:0 auto;position:relative}
.value-icon .ring{position:absolute;top:0;width:76px;height:76px;border-radius:50%}
.value h3{font-family:"Open Sans",sans-serif;font-size:12px;font-weight:600;margin-top:13px}
.value p{font-size:11px;line-height:22px;color:#555;margin:8px auto 0;width:260px}

/* newsletter */
.newsletter{height:265px;background:linear-gradient(180deg,#e3b12a,#d6a522)}
.newsletter h2{position:absolute;left:0;width:1200px;top:62px;text-align:center;color:var(--white);font-weight:700;font-size:30px}
.newsletter p{position:absolute;left:0;width:1200px;top:100px;text-align:center;color:var(--white);font-size:13px}
.email{position:absolute;left:349px;top:152px;width:415px;height:44px;border:1px solid rgba(255,255,255,.8);color:rgba(255,255,255,.9);font-size:12px;padding:13px 16px}
.btn-subscribe{position:absolute;left:767px;top:152px;width:89px;height:44px;background:var(--plum);color:var(--white);font-size:11px;font-weight:700;text-align:center;line-height:44px}

/* footer */
.site-footer{height:71px;background:var(--plum-deep);font-size:11px;color:#8c7396}
.site-footer .copy{position:absolute;left:172px;top:28px}
.site-footer .links{position:absolute;right:170px;top:28px}
</style>
</head>
<body>

<header class="site-header">
  <div class="brand">Heartline</div>
  <nav class="main-nav"><span>Home</span><span>About Us</span><span>Community</span><span>Blog</span></nav>
  <div class="nav-tools">
    <svg width="34" height="34" viewBox="0 0 34 34"><circle cx="17" cy="17" r="16" fill="#3b3b3b"/><circle cx="17" cy="13" r="5" fill="#e9e9e9"/><path d="M8 26c2-5 5-7 9-7s7 2 9 7" fill="#e9e9e9"/><circle cx="29" cy="5" r="4" fill="#d43b3b"/></svg>
    <svg width="14" height="14" viewBox="0 0 14 14"><circle cx="6" cy="6" r="4.5" fill="none" stroke="#333" stroke-width="1.8"/><path d="M9.5 9.5L13 13" stroke="#333" stroke-width="1.8"/></svg>
  </div>
</header>

<section class="hero">
  <div class="photo hero-photo" role="img" aria-label="Man in a red sweater smiling while working on a laptop against a painted wall"></div>
  <div class="hero-bars"></div>
  <h1>Find The<br><strong>Perfect Match</strong></h1>
  <p class="abs hero-lead">Duis aute irure dolor in reprehenderit in voluptate esse cillum dolore eu fugiat nulla pariatur</p>
  <div class="field" style="top:208px">Username</div>
  <div class="field" style="top:259px">Email Address</div>
  <div class="field" style="top:310px">Password</div>
  <div class="btn-signup">Sign Up</div>
  <div class="abs latest">Latest Registered Members</div>
  <div class="abs latest-arrows">‹ ›</div>
  <div class="avatar" style="left:624px" role="img" aria-label="Portrait of a new member"></div>
  <div class="avatar" style="left:770px" role="img" aria-label="Portrait of a new member"></div>
  <div class="avatar" style="left:912px" role="img" aria-label="Portrait of a new member"></div>
</section>

<section class="members">
  <h2 class="section-kicker" style="top:66px">Meet our</h2>
  <h2 class="section-title" style="top:100px">Active Members</h2>
  <div class="photo member-tile" style="left:89px;background:linear-gradient(135deg,#d9b8a0,#a8323a)" role="img" aria-label="Member portrait"></div>
  <div class="photo member-tile" style="left:298px;background:linear-gradient(135deg,#8a8f88,#2e2e2e)" role="img" aria-label="Member portrait"></div>
  <div class="photo member-tile" style="left:507px;background:linear-gradient(135deg,#e0e0e0,#6b5a4f)" role="img" aria-label="Member portrait"></div>
  <div class="photo member-tile" style="left:716px;background:linear-gradient(135deg,#c9b9a8,#2f4f86)" role="img" aria-label="Member portrait"></div>
  <div class="photo member-tile" style="left:922px;background:linear-gradient(135deg,#e8e4de,#8c6a58)" role="img" aria-label="Member portrait"></div>
  <div class="abs discover">DISCOVER ALL MEMBERS</div>
</section>

<section class="community">
  <h2 class="section-kicker" style="top:60px">Be Part of a</h2>
  <h2 class="section-title" style="top:92px">Real Community</h2>
  <p class="centered-copy" style="top:130px">Nemo enim ipsam voluptatem quia voluptas sit aspernatur<br>aut odit aut fugit sed quia consequuntur</p>
  <div class="tabs"><span class="tab is-active">Popular</span><span class="tab">Newest</span><span class="tab">Active</span><span class="tab">Alphabetical</span></div>

  <div class="group" style="left:255px;top:313px">
    <div class="group-pic" role="img" aria-label="Couple embracing"></div>
    <div class="group-badge">members<b>15</b></div>
    <div class="group-name">Couple</div>
    <p class="group-text">Quis nostrum exercitationem ullam corporis suscipit laboriosam</p>
    <div class="group-link">View group ▸</div>
  </div>
  <div class="group" style="left:632px;top:313px">
    <div class="group-pic" style="background:linear-gradient(135deg,#d8b79c,#8a5a3e)" role="img" aria-label="Woman smiling outdoors"></div>
    <div class="group-badge">members<b>25</b></div>
    <div class="group-name">Site Lovers</div>
    <p class="group-text">Quis nostrum exercitationem ullam corporis suscipit laboriosam</p>
    <div class="group-link">View group ▸</div>
  </div>
  <div class="group" style="left:255px;top:466px">
    <div class="group-pic" style="background:linear-gradient(135deg,#e2a94a,#6b3a1c)" role="img" aria-label="Burger and fries"></div>
    <div class="group-badge">members<b>35</b></div>
    <div class="group-name">Fast Food</div>
    <p class="group-text">Quis nostrum exercitationem ullam corporis suscipit laboriosam</p>
    <div class="group-link">View group ▸</div>
  </div>
  <div class="group" style="left:632px;top:466px">
    <div class="group-pic" style="background:linear-gradient(135deg,#c49a4a,#2a2420)" role="img" aria-label="Saxophone player"></div>
    <div class="group-badge">members<b>98</b></div>
    <div class="group-name">Jazz Lovers</div>
    <p class="group-text">Quis nostrum exercitationem ullam corporis suscipit laboriosam</p>
    <div class="group-link">View group ▸</div>
  </div>
</section>

<section class="events">
  <div class="abs events-shadow"></div>
  <div class="photo events-photo" role="img" aria-label="Friends in masks at a community party"></div>
  <h2 class="split-kicker" style="left:683px;top:118px">Be part of stimulating</h2>
  <h2 class="split-title" style="left:683px;top:152px">Community Events</h2>
  <p class="split-copy" style="left:683px;top:206px">Quis autem vel eum iure reprehenderit qui in ea velit esse quam nihil molestiae consequatur<br><em style="font-weight:600;color:#333">Share, discuss &amp; maybe find your Life Partner.</em></p>
  <div class="btn-gold" style="left:685px;top:301px;width:181px;height:41px;line-height:41px">Discover Community Events</div>
</section>

<section class="near">
  <h2>Find People Near You</h2>
  <div class="location">Location...
    <svg width="12" height="8" viewBox="0 0 12 8"><path d="M1 1l5 5 5-5" fill="none" stroke="#fff" stroke-width="1.6"/></svg>
  </div>
  <div class="btn-find">Find Now</div>
  <div class="place" style="left:341px" role="img" aria-label="City skyline"></div>
  <div class="place" style="left:450px;background:linear-gradient(135deg,#b8b0a0,#5c5a48)" role="img" aria-label="Historic city view"></div>
  <div class="place" style="left:557px;background:linear-gradient(135deg,#8ec0e0,#3e7a3a)" role="img" aria-label="Park with trees"></div>
  <div class="place" style="left:667px;background:linear-gradient(135deg,#a8b8c8,#3e4a58)" role="img" aria-label="Downtown street"></div>
  <div class="place" style="left:776px;background:linear-gradient(135deg,#c0c4c8,#40454a)" role="img" aria-label="Group of friends"></div>
</section>

<section class="matching">
  <div class="match-card">
    <div class="photo match-photo" style="left:0;background:linear-gradient(135deg,#7ca86a,#c8d4e0)" role="img" aria-label="Smiling woman with short blonde hair"></div>
    <div class="photo match-photo" style="left:215px;background:linear-gradient(135deg,#e8e8e8,#4a6ea0)" role="img" aria-label="Smiling man with glasses"></div>
    <div class="match-score"><span>89%</span></div>
    <div class="match-name" style="left:0">Helen Ward</div>
    <div class="match-name" style="left:215px">Martin Hale</div>
    <div class="abs" style="left:214px;top:240px;width:1px;height:58px;background:#ddd"></div>
    <div class="abs" style="left:0;top:240px;width:430px;height:1px;background:#ddd"></div>
  </div>
  <h2 class="split-kicker" style="left:685px;top:122px">An Effective</h2>
  <h2 class="split-title" style="left:685px;top:155px">Scientific Matchmaking</h2>
  <p class="split-copy" style="left:685px;top:210px;width:350px">Itaque earum rerum hic tenetur a sapiente delectus ut aut reiciendis voluptatibus maiores alias consequatur aut</p>
  <div class="btn-gold" style="left:685px;top:288px;width:145px;height:43px;line-height:43px">Subscribe Now</div>
</section>

<section class="values">
  <h2 class="section-kicker" style="top:60px">Let's Make Dating</h2>
  <h2 class="section-title" style="top:96px">More Human &amp; More Simple</h2>

  <div class="value" style="left:156px">
    <div class="value-icon">
      <div class="ring" style="left:0;background:#6b5a28"></div>
      <div class="ring" style="left:36px;background:var(--gold)"></div>
      <div class="ring" style="left:18px;background:var(--gold);border:4px solid #fff"></div>
      <svg class="abs" style="left:41px;top:26px" width="30" height="26" viewBox="0 0 30 26"><path d="M15 25S1 16 1 8a7 7 0 0 1 14-2 7 7 0 0 1 14 2c0 8-14 17-14 17z" fill="#fff"/></svg>
    </div>
    <h3>Talk to Real People</h3>
    <p>Nemo enim ipsam voluptatem quia voluptas sit aspernatur aut odit aut fugit</p>
  </div>
  <div class="value" style="left:451px">
    <div class="value-icon">
      <div class="ring" style="left:0;background:#4a4540"></div>
      <div class="ring" style="left:36px;background:#6e6862"></div>
      <div class="ring" style="left:18px;background:#5c5650;border:4px solid #fff"></div>
      <svg class="abs" style="left:42px;top:24px" width="28" height="28" viewBox="0 0 28 28"><circle cx="14" cy="14" r="12" fill="none" stroke="#fff" stroke-width="2.5"/><path d="M8 14l4 4 8-8" fill="none" stroke="#fff" stroke-width="2.5"/></svg>
    </div>
    <h3>Smooth &amp; Simple Features</h3>
    <p>Nemo enim ipsam voluptatem quia voluptas sit aspernatur aut odit aut fugit</p>
  </div>
  <div class="value" style="left:744px">
    <div class="value-icon">
      <div class="ring" style="left:0;background:var(--plum)"></div>
      <div class="ring" style="left:36px;background:var(--plum-mid)"></div>
      <div class="ring" style="left:18px;background:#5a2c6a;border:4px solid #fff"></div>
      <svg class="abs" style="left:44px;top:22px" width="24" height="30" viewBox="0 0 24 30"><path d="M6 13V9a6 6 0 0 1 12 0v4" fill="none" stroke="#fff" stroke-width="2.6"/><rect x="2" y="13" width="20" height="15" rx="2" fill="#fff"/><circle cx="12" cy="20" r="2.2" fill="#5a2c6a"/></svg>
    </div>
    <h3>Your Data is Safe</h3>
    <p>Nemo enim ipsam voluptatem quia voluptas sit aspernatur aut odit aut fugit</p>
  </div>
</section>

<section class="newsletter">
  <h2>Keep in Touch with the Community</h2>
  <p>Subscribe to our newsletter and stay updated with latest news &amp; events</p>
  <div class="email">Email address...</div>
  <div class="btn-subscribe">Subscribe</div>
</section>

<footer class="site-footer">
  <div class="copy">©Copyright information here</div>
  <div class="links">Home | About | Community | Privacy Policy | Blog | Contact Us</div>
</footer>

</body>
</html>
```